terras letterhead

We would like to create a new letterhead that our company will use for proposals, invoices, statements and letters. Our company name is Terra-Crafters. We are a landscape design/build and landscape maintenance company. We have a web site Terra-Crafters.example where our logo (the leaf with the lettering within it only) is displayed.

Industry/Entity Type

Graphic Design

Requirements
Must have
• Address and info on our current letterhead (uploaded)
Nice to have
• We would like the design to look presentable in grey scale as well as color.
Should not have
• Do not want to infringe much on the normal useable area within the normal print areas.

```html
<!DOCTYPE html>
<html lang="en">
<head>
<meta charset="utf-8">
<title>Terra-Crafters Letterhead</title>
<link rel="stylesheet" href="https://fonts.googleapis.com/css2?family=Domine:wght@700&display=swap">
<style>
  :root {
    --backdrop: #5a5a5c;
    --paper: #ffffff;
    --band: #dcdba4;
    --band-edge: #eeedcb;
    --brand-green: #1f3d22;
    --ink: #1e1e14;
    --rule: #6b6548;
  }
  * { margin: 0; padding: 0; box-sizing: border-box; }
  html, body {
    width: 1200px;
    height: 1000px;
    overflow: hidden;
    background: var(--backdrop);
  }
  .letterhead {
    position: absolute;
    left: 294px;
    top: 84px;
    width: 602px;
    height: 846px;
    background: var(--paper);
  }
  .header-band {
    position: absolute;
    left: 0;
    top: 0;
    width: 602px;
    height: 120px;
  }
  .brand-name {
    position: absolute;
    left: 18px;
    top: 34px;
    font-family: "Domine", Georgia, serif;
    font-weight: 700;
    font-size: 19px;
    letter-spacing: 0.3px;
    color: var(--brand-green);
  }
  .footer {
    position: absolute;
    left: 37px;
    top: 798px;
    width: 527px;
    border-top: 1px solid var(--rule);
    padding-top: 5px;
    text-align: center;
    font-family: "Domine", Georgia, serif;
    font-weight: 700;
    font-size: 11.2px;
    line-height: 15.5px;
    color: var(--ink);
  }
</style>
</head>
<body>
  <main class="letterhead">
    <svg class="header-band" viewBox="0 0 602 120" aria-hidden="true">
      <path fill="var(--band)" d="M0 0 H602 V12 C 480 4, 340 4, 265 45 C 200 82, 130 106, 55 106 C 30 106, 12 105, 0 104 Z"/>
      <path fill="none" stroke="var(--band-edge)" stroke-width="2.5" d="M0 101 C 14 102, 32 103, 55 103 C 128 103, 198 79, 262 43 C 338 2, 480 2, 602 9"/>
    </svg>
    <div class="brand-name">Terra-Crafters</div>

    <footer class="footer">
      <p class="contact-line">Phone: (555) 014-2290 | Fax: (555) 014-2291 | Email: service@terra-crafters.example</p>
      <p class="address-line">Web: terra-crafters.example | 418 Meadowbrook Lane Fernvale, NJ 07999</p>
    </footer>
  </main>
</body>
</html>
```